Brontal Land Associates Web Site

We need a website design for a new land purchasing and development business based in PEI. We are just regular guys trying a new adventure buying small parcels of land, doing the hard work seperating them into lots, building roads and selling off a dream location. We help folks like ourselves buy the lots, create a house plan and help get the project done.

We have a wordpress website, but no skills. The site should have our simple story and links to individual land development progects, currently we have 2. The larger project is on a golf course and images have been uploaded. We would like a map of the properities with locations on the properties you can click to see the views/ pictures. It would be great to have the ability to superimpose house images on the lot images. This would help prospects see the end results. I have attached some photos and logo's, however, they are not manditory.
The project would have to allow for us to update and maintain the site.

Target Market(s)

Visitors to PEI, typically from larger cities in Ontario and Maine. Golfers that want to live on a golf course.

Industry/Entity Type

Realestate (land development)

Coding

Coded - Design and coding required

Number of Pages Required

4 page

Requirements
Must have
• Allow fo us to maintain the site. Company overview page with story and contact information. Links to current realestate projects (developments). Project pages with the informaiton on the land and purchasing. Since this is land not houses, maps to the site, maps of the parcel, maps of the individual lots with the ability to review photos based on the views of that particular lot.
Nice to have
• The ability to upload and overlay a house picture on the lot. This would provide a visual of the final build.

```html
<!DOCTYPE html>
<html lang="en">
<head>
<meta charset="utf-8">
<title>Brontal Land Associates</title>
<link rel="stylesheet" href="https://fonts.googleapis.com/css2?family=Baloo+2:wght@600;700;800&family=Lato:wght@300;400;700;900&display=swap">
<style>
:root{
  --navy:#12285a;
  --navy-deep:#1c2741;
  --sky:#29aae1;
  --ink:#2a2a2a;
  --muted:#555b66;
  --band:#e9ebef;
  --white:#ffffff;
  --green-tick:#3aa35a;
}
*{box-sizing:border-box;margin:0;padding:0}
html,body{width:1200px;height:4675px;overflow:hidden}
body{position:relative;background:var(--white);font-family:"Lato",sans-serif;color:var(--ink)}
.abs{position:absolute}
.heading{font-family:"Baloo 2",sans-serif;font-weight:800;color:var(--navy);line-height:1}
.eyebrow{font-size:22px;color:var(--sky);font-weight:400}
.body-text{font-size:15px;line-height:26px;color:var(--ink)}
.btn{position:absolute;display:flex;align-items:center;justify-content:center;gap:6px;background:var(--sky);color:var(--white);font-weight:700;font-size:16px;border-radius:3px}
.btn .dot{width:8px;height:8px;border:2px solid var(--white);border-radius:50%}

/* hero */
.hero{position:absolute;left:0;top:0;width:1200px;height:637px;background:linear-gradient(180deg,#3d5169 0%,#6e7f8e 28%,#4e7a3a 42%,#4f8a33 70%,#3c6b25 100%)}
.topbar{position:absolute;right:0;top:0;width:474px;height:40px;background:var(--navy);border-bottom-left-radius:30px;color:var(--white);font-size:16px;display:flex;align-items:center;justify-content:flex-end;gap:22px;padding-right:100px}
.topbar span{display:flex;align-items:center;gap:6px}
.brand{position:absolute;display:flex;align-items:center;gap:12px;color:var(--white);font-family:"Lato",sans-serif;font-weight:900;font-size:22px}
.brand .mark{width:60px;height:60px;border-radius:50%;background:var(--white)}
.nav{position:absolute;top:64px;left:526px;font-size:16px;color:var(--white)}
.nav a{position:absolute;white-space:nowrap;color:var(--white);text-decoration:none}
.hero-title{position:absolute;left:0;width:1160px;text-align:center;color:var(--white)}
.hero-arrow{position:absolute;top:345px}

/* welcome */
.photo-disc{position:absolute;left:609px;top:684px;width:493px;height:490px;border-radius:50%;background:linear-gradient(160deg,#7fa0c8 0%,#b9c9d6 30%,#4f6a3c 48%,#b29252 70%,#5c6e3a 100%);border-left:10px solid var(--navy);border-top:10px solid var(--navy)}
.tag-tri{position:absolute;left:588px;top:962px}
.tag-text{position:absolute;left:596px;top:1050px;color:var(--white);font-family:"Baloo 2",sans-serif;font-weight:700;font-size:22px;line-height:38px}

/* projects */
.card{position:absolute;top:1465px;width:310px}
.card .thumb{height:210px;border-radius:3px}
.card h3{margin-top:33px;width:290px;font-size:17px;font-weight:700;line-height:25px;color:var(--ink)}
.card p{margin-top:6px;font-size:15px;line-height:23px;color:var(--muted)}

/* value */
.arch-photo{position:absolute;left:103px;top:2024px;width:438px;height:450px;border-radius:225px 225px 0 225px;background:radial-gradient(circle at 50% 70%,#a9c95a 0%,#8ab53c 40%,#5f8a2f 75%,#3e6424 100%)}
.arch-frame{position:absolute;left:118px;top:2018px;width:434px;height:458px;border-top:9px solid var(--navy);border-right:9px solid var(--navy);border-top-right-radius:225px}
.check-item{position:absolute;left:613px;width:490px;padding-left:28px;font-size:15px;line-height:26px;color:var(--muted)}
.check-item svg{position:absolute;left:0;top:3px}

/* testimonial */
.band{position:absolute;left:0;top:2602px;width:1200px;height:455px;background:var(--band)}
.round-arrow{position:absolute;width:40px;height:40px;border-radius:8px;background:var(--white);display:flex;align-items:center;justify-content:center;box-shadow:0 2px 5px rgba(0,0,0,.1)}

/* contact */
.info{position:absolute;width:240px}
.info h4{font-size:18px;font-weight:700;color:var(--navy)}
.info p{font-size:15px;line-height:24px;color:var(--ink);margin-top:4px}
.info-link{position:absolute;font-size:15px;font-weight:700;color:var(--sky);text-decoration:none}
.map-arch{position:absolute;left:612px;top:3149px;width:490px;height:574px;border-radius:245px 245px 0 0;background:linear-gradient(180deg,#eceef0,#dfe2e4)}
.map-arch-line{position:absolute;left:622px;top:3152px;width:472px;height:562px;border:2px solid var(--sky);border-radius:236px 236px 0 0}

/* subscribe */
.subscribe{position:absolute;left:94px;top:3859px;width:1004px;height:336px;border-radius:22px;background:linear-gradient(135deg,#17356f,#102a5c);border:6px solid #9aa1ad;text-align:center;color:var(--white)}
.email-field{position:absolute;left:133px;top:206px;width:608px;height:55px;background:var(--white);border-radius:2px 0 0 2px;display:flex;align-items:center;gap:12px;padding-left:22px;color:#555;font-size:15px}
.email-btn{position:absolute;left:741px;top:206px;width:136px;height:55px;background:var(--sky);display:flex;align-items:center;justify-content:center;gap:6px;font-weight:700;font-size:16px}

/* footer */
.footer{position:absolute;left:0;top:4269px;width:1200px;height:406px;background:var(--navy-deep);color:#e6e8ee}
.footer h5{position:absolute;font-size:18px;font-weight:700;color:var(--sky)}
.footer ul{position:absolute;list-style:none;font-size:15px}
.footer li{height:38.5px;display:flex;gap:12px;align-items:flex-start}
</style>
</head>
<body>

<!-- HERO -->
<header class="hero" role="img" aria-label="Wide golf course fairway under a cloudy sky"></header>
<div class="topbar">
  <span><svg width="14" height="11" viewBox="0 0 14 11"><rect width="14" height="11" rx="1" fill="#29aae1"/><path d="M0 1l7 5 7-5" stroke="#12285a" fill="none" stroke-width="1.4"/></svg>hello@brontalland.com</span>
  <span><svg width="14" height="14" viewBox="0 0 24 24"><path d="M6.6 10.8a15 15 0 006.6 6.6l2.2-2.2c.3-.3.7-.4 1-.2 1.1.4 2.3.6 3.6.6.6 0 1 .4 1 1V20c0 .6-.4 1-1 1A17 17 0 013 4c0-.6.4-1 1-1h3.5c.6 0 1 .4 1 1 0 1.3.2 2.5.6 3.6.1.3 0 .7-.2 1z" fill="#29aae1"/></svg>01 555 204 318</span>
</div>
<div class="brand" style="left:100px;top:22px">
  <div class="mark"></div>
  <div style="line-height:1.05">Brontal Land<br><span style="font-size:13px;font-weight:400">Associates</span></div>
</div>
<nav class="nav">
  <a style="left:0;color:var(--sky)">Home</a>
  <a style="left:95px">About</a>
  <a style="left:187px">Recent Project</a>
  <a style="left:347px">Map</a>
</nav>
<div class="btn" style="left:942px;top:56px;width:105px;height:44px">Contact <span class="dot"></span></div>
<div class="hero-title" style="top:248px;font-weight:300;font-size:70px">Discover</div>
<div class="hero-title heading" style="top:330px;color:var(--white);font-size:76px">Most Suitable Land</div>
<div class="btn" style="left:496px;top:434px;width:150px;height:52px">Get Started <span class="dot"></span></div>
<svg class="hero-arrow" style="left:98px" width="24" height="40" viewBox="0 0 24 40"><path d="M20 2L4 20l16 18" stroke="#fff" stroke-width="2.5" fill="none"/></svg>
<svg class="hero-arrow" style="left:1080px" width="24" height="40" viewBox="0 0 24 40"><path d="M4 2l16 18L4 38" stroke="#fff" stroke-width="2.5" fill="none"/></svg>

<!-- WELCOME -->
<section>
  <div class="abs eyebrow" style="left:98px;top:778px">Welcome to</div>
  <h1 class="abs heading" style="left:98px;top:808px;font-size:66px">Brontal Land</h1>
  <p class="abs body-text" style="left:98px;top:886px;width:410px">Lorem ipsum dolor sit amet, consectetur adipiscing elit. Cras at ornare quam. Fusce pellentesque mauris dui, ut sollicitudin quam ornare sed. Mauris egestas risus vitae velit tempor, sit amet portor elit frigila. Vivamus vehicula condimentum dictum.</p>
  <div class="btn" style="left:98px;top:1045px;width:130px;height:55px">Read More <span class="dot"></span></div>
  <div class="photo-disc" role="img" aria-label="Golden meadow grass beside a country road with hills and houses behind"></div>
  <svg class="tag-tri" width="240" height="212" viewBox="0 0 240 212"><path d="M0 0L240 212H0z" fill="#12285a"/></svg>
  <div class="tag-text">Land<br>Purchasing<br>&amp; Development</div>
</section>

<!-- RECENT PROJECTS -->
<section>
  <h2 class="abs heading" style="left:0;width:1200px;text-align:center;top:1368px;font-size:62px">Our Recent Project</h2>
  <article class="card" style="left:100px">
    <div class="thumb" role="img" aria-label="Green lawn with trees under a blue sky" style="background:linear-gradient(180deg,#6ea7dc 0%,#a9cbe6 35%,#4f8a30 55%,#7fbd3c 100%)"></div>
    <h3>Donec vel fringilla leo aliquam laoreet</h3>
    <p>Lorem ipsum dolor sit conectetur adipiscing elit, sed do eiusmod tempor incididunt ut labore et dolore magna aliqua.</p>
  </article>
  <div class="btn" style="left:96px;top:1839px;width:128px;height:53px">Read More <span class="dot"></span></div>
  <article class="card" style="left:445px">
    <div class="thumb" role="img" aria-label="Open pasture under tall white clouds" style="background:linear-gradient(180deg,#2f6aa8 0%,#a8c2db 45%,#dfe8ef 60%,#3e7a2e 78%,#5d9a35 100%)"></div>
    <h3>Donec vel fringilla leo aliquam laoreet</h3>
    <p>Lorem ipsum dolor sit conectetur adipiscing elit, sed do eiusmod tempor incididunt ut labore et dolore magna aliqua.</p>
  </article>
  <div class="btn" style="left:441px;top:1839px;width:128px;height:53px">Read More <span class="dot"></span></div>
  <article class="card" style="left:790px">
    <div class="thumb" role="img" aria-label="Rolling green fairway below a pale blue sky" style="background:linear-gradient(180deg,#4f8fd8 0%,#9cc3ea 40%,#7fbf3a 58%,#5aa02c 100%)"></div>
    <h3>Donec vel fringilla leo aliquam laoreet</h3>
    <p>Lorem ipsum dolor sit conectetur adipiscing elit, sed do eiusmod tempor incididunt ut labore et dolore magna aliqua.</p>
  </article>
  <div class="btn" style="left:788px;top:1839px;width:128px;height:53px">Read More <span class="dot"></span></div>
</section>

<!-- VALUE -->
<section>
  <div class="arch-frame"></div>
  <div class="arch-photo" role="img" aria-label="Sunlit grass field bordered by trees"></div>
  <div class="abs eyebrow" style="left:613px;top:2022px">Our Value</div>
  <h2 class="abs heading" style="left:613px;top:2056px;font-size:66px;line-height:72px">Value We Give<br>To You</h2>
  <p class="abs" style="left:613px;top:2202px;width:500px;font-size:15px;font-weight:700;line-height:26px">Aliquam erat volutpat. Integer accumsan ultrices dui eu efficitur. Vestibulum pulvinar id nunc et mollis.</p>
  <div class="check-item" style="top:2280px"><svg width="18" height="18" viewBox="0 0 18 18"><circle cx="9" cy="9" r="9" fill="#3aa35a"/><path d="M5 9.3l2.6 2.5L13 6.5" stroke="#fff" stroke-width="2" fill="none"/></svg>Mauris egestas risus vitae velit tempor, sit amet rtor elit fringilla. Vivamus vehicula condimentum dictum.</div>
  <div class="check-item" style="top:2352px"><svg width="18" height="18" viewBox="0 0 18 18"><circle cx="9" cy="9" r="9" fill="#3aa35a"/><path d="M5 9.3l2.6 2.5L13 6.5" stroke="#fff" stroke-width="2" fill="none"/></svg>Cras sit amet convallis ligula. Nunc sed turpis sit amet massa consectetur varius vitae sit amet est. Sed lacus tortor,</div>
  <div class="check-item" style="top:2428px">Donec hendrerit elit elit, lobortis auctor lorem ullamcorper vel. Maecenas fringilla tristique elit eu finibus. Sed ultriciest in luctus.</div>
</section>

<!-- TESTIMONIAL -->
<section class="band">
  <p class="abs" style="left:200px;top:128px;width:800px;font-size:23px;font-weight:700;line-height:42px;color:var(--ink)">“Aenean magna nibh, lacinia quis sagittis vel, suscipit plrat libero. Donec eleifend lectus nec erat lobortis, ut fau enim sodales. Suspendisse vehicula et enim dictum rutrum. Cras sit amet convallis ligula. “</p>
  <div class="round-arrow" style="left:99px;top:215px"><svg width="10" height="16" viewBox="0 0 10 16"><path d="M8 2L2 8l6 6" stroke="#222" stroke-width="2" fill="none"/></svg></div>
  <div class="round-arrow" style="left:1061px;top:215px"><svg width="10" height="16" viewBox="0 0 10 16"><path d="M2 2l6 6-6 6" stroke="#222" stroke-width="2" fill="none"/></svg></div>
  <svg class="abs" style="left:625px;top:262px" width="120" height="80" viewBox="0 0 120 80"><path d="M3 3C15 40 50 70 115 70" stroke="#29aae1" stroke-width="2" fill="none"/><path d="M104 60l11 10-12 7" stroke="#29aae1" stroke-width="2" fill="none"/></svg>
  <div class="abs" style="left:640px;top:306px;width:250px;text-align:right;font-size:22px;letter-spacing:2px;font-weight:700;color:var(--navy)">Owen Maddox</div>
  <div class="abs" style="left:640px;top:342px;width:250px;text-align:right;font-size:13px;color:var(--sky)">Prince Edward Island</div>
  <div class="abs" role="img" aria-label="Client portrait" style="left:900px;top:286px;width:92px;height:92px;border-radius:50%;background:linear-gradient(180deg,#d9dde3,#aeb6c0);border:5px solid var(--white);box-shadow:0 4px 10px rgba(0,0,0,.2)"></div>
</section>

<!-- CONTACT -->
<section>
  <div class="abs eyebrow" style="left:98px;top:3226px">Contact Us</div>
  <h2 class="abs heading" style="left:98px;top:3255px;font-size:66px;line-height:68px">Easy to<br>Contact Us</h2>

  <svg class="abs" style="left:99px;top:3442px" width="20" height="20" viewBox="0 0 24 24"><path d="M6.6 10.8a15 15 0 006.6 6.6l2.2-2.2c.3-.3.7-.4 1-.2 1.1.4 2.3.6 3.6.6.6 0 1 .4 1 1V20c0 .6-.4 1-1 1A17 17 0 013 4c0-.6.4-1 1-1h3.5c.6 0 1 .4 1 1 0 1.3.2 2.5.6 3.6.1.3 0 .7-.2 1z" fill="none" stroke="#29aae1" stroke-width="2"/></svg>
  <div class="info" style="left:142px;top:3428px"><h4>Call</h4><p>01 555 204 318</p></div>
  <a class="info-link" style="left:142px;top:3520px">Call Now</a>

  <svg class="abs" style="left:358px;top:3442px" width="20" height="24" viewBox="0 0 20 24"><path d="M10 1a8 8 0 00-8 8c0 6 8 14 8 14s8-8 8-14a8 8 0 00-8-8z" fill="#29aae1"/><circle cx="10" cy="9" r="3" fill="#fff"/></svg>
  <div class="info" style="left:401px;top:3428px"><h4>Location</h4><p>18 Fairway Road,<br>Summerside, PEI</p></div>
  <a class="info-link" style="left:401px;top:3520px">Map</a>

  <svg class="abs" style="left:99px;top:3632px" width="20" height="15" viewBox="0 0 20 15"><rect width="20" height="15" rx="1" fill="#29aae1"/><path d="M1 1l9 7 9-7" stroke="#fff" fill="none" stroke-width="1.6"/></svg>
  <div class="info" style="left:142px;top:3606px"><h4>Message</h4><p>hello@brontalland.com</p></div>
  <a class="info-link" style="left:142px;top:3700px">Message Now</a>

  <svg class="abs" style="left:357px;top:3628px" width="22" height="22" viewBox="0 0 22 22"><path d="M11 1C5.5 1 1 5 1 10c0 2.4 1 4.5 2.7 6.1L3 21l4.6-2.4c1 .3 2.2.4 3.4.4 5.5 0 10-4 10-9S16.5 1 11 1z" fill="#29aae1"/><circle cx="7" cy="10" r="1.3" fill="#fff"/><circle cx="11" cy="10" r="1.3" fill="#fff"/><circle cx="15" cy="10" r="1.3" fill="#fff"/></svg>
  <div class="info" style="left:401px;top:3606px"><h4>Chat</h4><p>01 555 204 318</p></div>
  <a class="info-link" style="left:401px;top:3700px">Chat Now</a>

  <div class="map-arch" role="img" aria-label="Subdivision site plan showing numbered lots and roads"></div>
  <div class="map-arch-line"></div>
</section>

<!-- SUBSCRIBE -->
<section class="subscribe">
  <h2 style="position:absolute;left:0;width:992px;top:34px;font-size:66px;line-height:1"><span style="font-family:'Lato',sans-serif;font-weight:300">Subscribe </span><span style="font-family:'Baloo 2',sans-serif;font-weight:800">For Update</span></h2>
  <p style="position:absolute;left:120px;width:752px;top:130px;font-size:15px;line-height:27px">Donec consectetur euismod enim, ut convallis lacus. Aenean mauris nibh, molestie eget ipsum a, iaculis dictum felis. Etiam nec commodo est.</p>
  <div class="email-field"><svg width="16" height="12" viewBox="0 0 16 12"><rect width="16" height="12" rx="1" fill="#9aa1ad"/><path d="M1 1l7 5 7-5" stroke="#fff" fill="none" stroke-width="1.4"/></svg>Enter Email Address</div>
  <div class="email-btn">Subscribe <span style="width:8px;height:8px;border:2px solid #fff;border-radius:50%"></span></div>
</section>

<!-- FOOTER -->
<footer class="footer">
  <div class="brand" style="left:100px;top:78px">
    <div class="mark" style="width:70px;height:70px"></div>
    <div style="line-height:1.05;font-size:24px">Brontal Land<br><span style="font-size:13px;font-weight:400">Associates</span></div>
  </div>
  <p style="position:absolute;left:100px;top:180px;width:320px;font-size:15px;line-height:30px">Orci varius natoque penatibus et magnis dis parturient montes, nascetur ridiculus mus. Nulla cursus nulla magna</p>
  <h5 style="left:459px;top:74px">Quick Links</h5>
  <ul style="left:466px;top:128px">
    <li><span>›</span>Home</li><li><span>›</span>About</li><li><span>›</span>Recent Project</li><li><span>›</span>Map</li><li><span>›</span>Contact</li>
  </ul>
  <h5 style="left:675px;top:74px">Projects</h5>
  <ul style="left:682px;top:128px">
    <li><span>›</span>Vehicula sed</li><li><span>›</span>Ut neque nisl</li><li><span>›</span>Tempor</li><li><span>›</span>Maecsquis</li><li><span>›</span>Quis nisl pla</li>
  </ul>
  <div style="position:absolute;left:850px;top:138px;width:60px;height:60px;border-radius:50%;background:#8bb77a"></div>
  <div style="position:absolute;left:926px;top:154px;font-size:22px;font-weight:700;color:var(--white)">Crestline Links</div>
  <div style="position:absolute;left:100px;top:352px;font-size:14px;color:#9aa1ad;white-space:nowrap">© 2022 <span style="color:var(--sky);font-weight:700">Brontal Land</span>. All right reserved</div>
  <div style="position:absolute;left:350px;top:362px;width:752px;height:1px;background:#4a5570"></div>
</footer>

</body>
</html>
```